2367 Halvorsen Avenue Medical Centre

We are looking for a design for new medical clinic.
We are accepting new patients at this new medical centre grand opening. Walk-ins are welcome.
Our cardiac and vascular surgical specialists are department heads at St Alder's Hospital, a leading teaching hospital in Toronto. These specialists will see cardiovascular consults are well as pre-surgical and post-surgical consultations and follow-ups.
Our lab is affiliated with several nuclear medicine clinics in the GTA.
Our Services Includes:
Family Practice
Cardiology Diagnostics
Cardiac & Vascular Surgical Consultation
Ultrasound & Vascular Testing
Open 6 days a week.
Ample Free Parking
Friendly Staffs

Target Market(s)

New Patients. Families of any age. Ethnic groups including Asians & Africans.

Industry/Entity Type

Medical

Font styles to use
Serif
Sans Serif
Decorative
Script
Other font styles liked:
• Arial calibri, verdana

Requirements
Must have
• Address:
• 2367 Halvorsen Avenue East
• Unit 225
• Scarborough, Ontario
• K7T 2P4
• Tel: (416) 555-0148
Nice to have
• Caring and inviting environment.
• Simple but classy.
• Standout colors.
Should not have
• Busy images. Aside from this, any ideas are welcome.

```html
<!DOCTYPE html>
<html lang="en">
<head>
<meta charset="utf-8">
<title>Grand Opening – 2367 Halvorsen Avenue Medical Centre</title>
<link rel="stylesheet" href="https://fonts.googleapis.com/css2?family=Montserrat:wght@400;600;700;800&family=Open+Sans:wght@400;600&display=swap">
<style>
  :root{
    --bg:#a9a9ab;
    --paper:#f3f6f9;
    --paper-cool:#e2e9ef;
    --blue:#1f9fe0;
    --blue-deep:#1565b4;
    --blue-mid:#2b86cf;
    --sky:#39b4ec;
    --indigo:#2c2f78;
    --purple:#4d4b9c;
    --ink:#2d2d3a;
    --white:#ffffff;
  }
  *{box-sizing:border-box;margin:0;padding:0}
  html,body{width:1200px;height:955px;overflow:hidden}
  body{background:var(--bg);font-family:"Open Sans",Arial,sans-serif;position:relative}

  .flyer{position:absolute;left:282px;top:27px;width:636px;height:900px;
    background:linear-gradient(180deg,var(--white) 0%,var(--paper) 55%,var(--paper-cool) 100%);
    overflow:hidden;box-shadow:0 6px 18px rgba(0,0,0,.25)}

  .hero-photo{position:absolute;left:0;top:0;width:636px;height:380px;
    background:linear-gradient(100deg,#e4e9ee 0%,#c9d6e2 28%,#9cc9ea 55%,#5eaee2 78%,#3d98d6 100%)}
  .hero-curve{position:absolute;left:0;top:0}

  .hours-badge{position:absolute;left:455px;top:160px;width:150px;height:150px;border-radius:50%;
    background:radial-gradient(circle at 40% 35%,#c8ecfb 0%,#6fcaf2 60%,#3aa9e3 100%);
    border:5px solid #6a62b8;display:flex;flex-direction:column;align-items:center;justify-content:center;
    font-family:"Montserrat",sans-serif;color:var(--indigo);line-height:1;text-align:center;transform:rotate(-12deg)}
  .hours-badge .big{font-weight:800;font-size:30px}
  .hours-badge .small{font-weight:600;font-size:21px;margin-top:3px}

  .ribbon{position:absolute;left:0;top:395px;width:636px;height:80px}
  .ribbon-title{position:absolute;left:0;top:405px;width:636px;text-align:center;
    font-family:"Montserrat",sans-serif;font-weight:800;font-size:50px;letter-spacing:1px;color:var(--white)}

  .tagline{position:absolute;left:0;top:488px;width:636px;text-align:center;
    font-family:"Montserrat",sans-serif;font-weight:600;font-size:22px;color:var(--purple);letter-spacing:.5px}
  .intro{position:absolute;left:60px;top:524px;width:516px;text-align:center;font-size:12px;line-height:1.45;color:var(--ink)}

  .services{position:absolute;left:0;top:615px;width:636px;height:120px;
    background:linear-gradient(90deg,var(--blue-deep) 0%,var(--blue-mid) 50%,var(--blue) 100%)}
  .services-tab{position:absolute;left:0;top:-18px;padding:7px 26px 7px 16px;background:#5a5aa8;color:var(--white);
    font-family:"Montserrat",sans-serif;font-weight:800;font-size:15px;letter-spacing:1px;
    clip-path:polygon(0 0,92% 0,100% 100%,0 100%)}
  .services-col{position:absolute;top:32px;list-style:none}
  .services-col.left{left:40px}
  .services-col.right{left:310px;padding-left:22px;border-left:1px solid rgba(255,255,255,.35);height:64px}
  .services-col li{display:flex;align-items:center;gap:8px;color:var(--white);font-size:13.5px;margin-bottom:14px;white-space:nowrap}
  .services-col svg{flex:none}

  .perks{position:absolute;top:752px;display:flex;align-items:center;gap:6px;
    font-family:"Montserrat",sans-serif;font-weight:700;font-size:15px;color:var(--ink)}
  .perks.left{left:150px}
  .perks.right{left:380px}

  .booking{position:absolute;left:40px;top:795px}
  .booking-label{display:inline-block;padding:6px 18px;background:linear-gradient(90deg,#3f86cc,#2fa3e3);border-radius:6px;
    color:var(--white);font-family:"Montserrat",sans-serif;font-weight:800;font-size:16px;letter-spacing:1px}
  .booking-phone{font-family:"Montserrat",sans-serif;font-weight:800;font-size:44px;color:var(--purple);margin-top:2px;letter-spacing:1px}

  .address{position:absolute;left:392px;top:792px;display:flex;gap:10px;padding-left:16px;border-left:1px solid #c4cfd8;font-style:normal}
  .address p{font-size:12.5px;line-height:1.35;color:var(--ink);font-weight:600;white-space:nowrap}

  .edge-stripe{position:absolute;left:0;bottom:0;width:636px;height:8px;background:linear-gradient(90deg,var(--blue-deep),var(--sky))}
</style>
</head>
<body>
<main class="flyer">
  <div class="hero-photo" role="img" aria-label="Photo of a smiling team of doctors and nurses in white coats and blue scrubs with stethoscopes"></div>
  <svg class="hero-curve" width="636" height="400" viewBox="0 0 636 400" aria-hidden="true">
    <path d="M0,330 Q330,395 636,110 L636,400 L0,400 Z" fill="#ffffff"/>
    <path d="M0,318 Q320,380 636,95" fill="none" stroke="#1f9fe0" stroke-width="14"/>
    <path d="M0,338 Q330,400 636,122" fill="none" stroke="#39b4ec" stroke-width="5"/>
  </svg>

  <div class="hours-badge"><span class="big">OPEN</span><span class="small">6 DAYS</span><span class="small">A WEEK</span></div>

  <svg class="ribbon" width="636" height="80" viewBox="0 0 636 80" aria-hidden="true">
    <defs><linearGradient id="ribbonFill" x1="0" x2="1"><stop offset="0" stop-color="#1a5fae"/><stop offset="1" stop-color="#2a94dc"/></linearGradient></defs>
    <polygon points="0,18 36,18 36,72 0,72 14,45" fill="#2c2f78"/>
    <polygon points="636,18 600,18 600,72 636,72 622,45" fill="#2c2f78"/>
    <rect x="24" y="6" width="588" height="62" fill="url(#ribbonFill)"/>
  </svg>
  <h1 class="ribbon-title">GRAND OPENING</h1>

  <h2 class="tagline">ACCEPTING WALK-IN PATIENTS.</h2>
  <p class="intro">Our cardiac and vascular surgical specialists are department heads at St Alder's Hospital, a leading teaching hospital in Toronto. These specialists will see cardiovascular consults are well as pre-surgical and post-surgical consultations and follow-ups.</p>

  <section class="services">
    <div class="services-tab">OUR SERVICES</div>
    <ul class="services-col left">
      <li><svg width="20" height="20" viewBox="0 0 20 20" fill="none" stroke="#b9b6f0" stroke-width="2"><path d="M4 2v6a4 4 0 0 0 8 0V2M8 12v2a4 4 0 0 0 8 0v-3"/><circle cx="16" cy="9" r="2"/></svg>Family Practice</li>
      <li><svg width="20" height="20" viewBox="0 0 20 20" fill="none" stroke="#b9b6f0" stroke-width="2"><path d="M4 2v6a4 4 0 0 0 8 0V2M8 12v2a4 4 0 0 0 8 0v-3"/><circle cx="16" cy="9" r="2"/></svg>Cardiology Diagnostics</li>
    </ul>
    <ul class="services-col right">
      <li><svg width="20" height="20" viewBox="0 0 20 20" fill="none" stroke="#b9b6f0" stroke-width="2"><path d="M4 2v6a4 4 0 0 0 8 0V2M8 12v2a4 4 0 0 0 8 0v-3"/><circle cx="16" cy="9" r="2"/></svg>Cardiac &amp; Vascular Surgical Consultation</li>
      <li><svg width="20" height="20" viewBox="0 0 20 20" fill="none" stroke="#b9b6f0" stroke-width="2"><path d="M4 2v6a4 4 0 0 0 8 0V2M8 12v2a4 4 0 0 0 8 0v-3"/><circle cx="16" cy="9" r="2"/></svg>Ultrasound &amp; Vascular</li>
    </ul>
  </section>

  <p class="perks left"><svg width="14" height="14" viewBox="0 0 14 14"><path d="M2 7l3 4 7-9" fill="none" stroke="#4d4b9c" stroke-width="2.4"/></svg>Ample Free Parking</p>
  <p class="perks right"><svg width="14" height="14" viewBox="0 0 14 14"><path d="M2 7l3 4 7-9" fill="none" stroke="#4d4b9c" stroke-width="2.4"/></svg>Friendly Staffs</p>

  <div class="booking">
    <span class="booking-label">TO BOOK APPOINTMENT</span>
    <p class="booking-phone">(416) 555-0148</p>
  </div>

  <address class="address">
    <svg width="18" height="24" viewBox="0 0 18 24"><path d="M9 1a8 8 0 0 0-8 8c0 6 8 14 8 14s8-8 8-14a8 8 0 0 0-8-8z" fill="#1f9fe0"/><circle cx="9" cy="9" r="3" fill="#fff"/></svg>
    <p>2367 Halvorsen Avenue East<br>Unit 225<br>Scarborough, Ontario<br>K7T 2P4</p>
  </address>

  <div class="edge-stripe"></div>
</main>
</body>
</html>
```